How BVKT works! a view of the innerworkings of a national medical specialty society

UPDATE 5/25/20 - 2nd page of this design entitled Zero-Based Committee Model. JPG image attached. Please use the same color scheme - this has minimal committee structure.

I need a graphic design, part infogram and part story board that explains the governance/operations of 2 sister nonprofit organizations - Lindenfield Academy of Orthopaedic Surgery and Guild of Orthopaedic Surgery (both referred to as BVKT). The Academy's color is red; the Association's color is blue. One board of directors in the center for both organizations. [NOTE: orthopaedic is spelled with an "a" after the letter "p".]

I uploaded a rough drawing, the BVKT logo and an example of the type of complicated operations I'd like to depict in the image.

Surrounding BVKT is a set of 4 councils - Education, Research & Quality, Membership, Advocacy. The Council on Advocacy (under the Association blue color) has an affiliated political action committee - PAC. The COA and PAC should be on the association (blue) side and beyond the COA and PAC should be an image of the US capital building and patients.

Four committees report to the board of directors - Committee on Ethics and Outside Interests (CEOI), Board of Councilors (BOC) and Board of Specialty Societies (BOS), and the Professional Compliance Program committees (PCP). Three committees report to BVKT members - Nominating Committee (NC), Bylaws Committee (BC) and Resolutions Committee (RC).

Each Council has 10 subcommittees under it.

The NC has 6 members - the 2nd past president appointed by the BOD; 1 member appointed jointly by the BOC and BOS; and 4 members elected by the membership.

The BOC has 100 members appointed by societies in each of the 50 states (an image of the US with the letters SOS).

The BOS members are appointed by 21 smaller specialty societies (use acronyms BRTWQ, GLU, PWIB, NUDO, EV, YT, FWUL, ZQMEU, DBIW, TIGK, UFBZK, IWNLE, ZCKW, VHYU, NGBE, TKW, DUWO, QETF, UWB, KIPEW, BWH).

The Board of Directors is composed of 16 individuals - 4 in the presidential line (president, 1st and 2nd vice presidents and the past president); 3 are appointed by the BOC; 3 are appointed by the BOS; and the remaining 6 are elected by the members.

There are 2 governing documents that circulate around the organizations, bylaws amendments and resolutions. Each starts with the BOC and BOS simultaneously, moves up to the Board of Directors, goes out to their respective committees (BC and RC) and each committee is sent to the outside edges of the picture where the members stand. Members should fill in the gaps all the way around the outside of the organization.

Target Market(s)

members of this organization - orthopaedic surgeons

Industry/Entity Type

Healthcare

Font styles to use
Sans Serif

Colors
3276b5
3277b5
cfdeed
ec1f27
f04a50
f59296
acd136
886aae
fbee3d

Requirements
Must have
• I'd like this to be a village, with the main organization at the center as the biggest structure, the councils, commitees and BOS and BOS units around it as smaller structures. There should be roads running throughout to connect the various buildings and the people.
primary organization colors red (academy) and blue (association)

```html
<!DOCTYPE html>
<html lang="en">
<head>
<meta charset="utf-8">
<title>How BVKT Works – Governance Map</title>
<link href="https://fonts.googleapis.com/css2?family=Open+Sans:ital,wght@0,400;0,700;1,400&display=swap" rel="stylesheet">
<style>
  :root {
    --bg: #efefef;
    --ink: #111111;
    --white: #ffffff;
    --red: #e31e26;
    --red-dark: #b50d14;
    --orange: #f07a12;
    --orange-dark: #e2531f;
    --green: #0bb844;
    --green-dark: #028a34;
    --blue: #3f8bd0;
    --blue-dark: #1e5a9a;
    --purple: #8f74bd;
    --purple-dark: #6b4f98;
    --dark-top: #4a4a4a;
    --dark-bottom: #111111;
  }
  html, body { margin: 0; padding: 0; overflow: hidden; background: var(--bg); }
  .canvas { width: 1200px; height: 809px; display: block; }
  svg text { font-family: "Open Sans", "Segoe UI", Arial, sans-serif; }
  .unit-label { font-weight: 700; fill: var(--white); text-anchor: middle; dominant-baseline: central; }
  .unit-label.xl { font-size: 46px; }
  .unit-label.lg { font-size: 34px; }
  .unit-label.md { font-size: 31px; }
  .society-cell { fill: var(--green-dark); stroke: var(--white); stroke-width: 2; }
  .society-label { font-size: 14px; font-weight: 700; fill: var(--white); text-anchor: middle; dominant-baseline: central; }
  .dash { fill: none; stroke-width: 3.5; stroke-dasharray: 9 6; }
  .dash.black { stroke: var(--ink); }
  .dash.orange { stroke: var(--orange); }
  .dash.green { stroke: var(--green); }
  .dash.red { stroke: var(--red); }
  .dash.purple { stroke: var(--purple); }
  .frame { fill: none; stroke: var(--ink); stroke-width: 4; stroke-dasharray: 10 6; }
  .key-text { font-size: 22px; font-style: italic; fill: var(--ink); }
  .spoke { stroke: var(--ink); stroke-width: 3; }
  .burst-arrow { stroke: var(--ink); stroke-width: 2.5; }
  .sat-ring { fill: var(--ink); }
  .sat-white { fill: var(--white); }
  .sat-dark { fill: #1a1a1a; }
  .sat-blue { fill: #3577b6; }
  .sat-purple { fill: #8a6fb7; }
  .seat { fill: var(--white); stroke-width: 3; }
</style>
</head>
<body>
<svg class="canvas" viewBox="0 0 2325 1568" xmlns="http://www.w3.org/2000/svg" aria-label="How BVKT works: governance map of Lindenfield Academy and Guild of Orthopaedic Surgery">
  <defs>
    <linearGradient id="g-dark" x1="0" y1="0" x2="0" y2="1"><stop offset="0" stop-color="var(--dark-top)"/><stop offset="1" stop-color="var(--dark-bottom)"/></linearGradient>
    <linearGradient id="g-orange" x1="0" y1="0" x2="0" y2="1"><stop offset="0" stop-color="#ff8a00"/><stop offset="1" stop-color="var(--orange-dark)"/></linearGradient>
    <linearGradient id="g-green" x1="0" y1="0" x2="0" y2="1"><stop offset="0" stop-color="#0ccb4a"/><stop offset="1" stop-color="var(--green-dark)"/></linearGradient>
    <linearGradient id="g-blue" x1="0" y1="0" x2="0" y2="1"><stop offset="0" stop-color="var(--blue)"/><stop offset="1" stop-color="var(--blue-dark)"/></linearGradient>
    <linearGradient id="g-purple" x1="0" y1="0" x2="0" y2="1"><stop offset="0" stop-color="#9f86c9"/><stop offset="1" stop-color="var(--purple-dark)"/></linearGradient>
    <linearGradient id="g-red" x1="0" y1="0" x2="0" y2="1"><stop offset="0" stop-color="#f8444b"/><stop offset="1" stop-color="var(--red-dark)"/></linearGradient>
    <linearGradient id="g-stone" x1="0" y1="0" x2="0" y2="1"><stop offset="0" stop-color="#d9d9d9"/><stop offset="1" stop-color="#8c8c8c"/></linearGradient>

    <marker id="a-black" viewBox="0 0 10 10" refX="8" refY="5" markerWidth="5" markerHeight="5" orient="auto-start-reverse"><path d="M0 0 L10 5 L0 10 Z" fill="#111"/></marker>
    <marker id="a-orange" viewBox="0 0 10 10" refX="8" refY="5" markerWidth="5" markerHeight="5" orient="auto"><path d="M0 0 L10 5 L0 10 Z" fill="#f07a12"/></marker>
    <marker id="a-green" viewBox="0 0 10 10" refX="8" refY="5" markerWidth="5" markerHeight="5" orient="auto"><path d="M0 0 L10 5 L0 10 Z" fill="#0bb844"/></marker>
    <marker id="a-red" viewBox="0 0 10 10" refX="8" refY="5" markerWidth="5" markerHeight="5" orient="auto"><path d="M0 0 L10 5 L0 10 Z" fill="#e31e26"/></marker>
    <marker id="a-purple" viewBox="0 0 10 10" refX="8" refY="5" markerWidth="5" markerHeight="5" orient="auto"><path d="M0 0 L10 5 L0 10 Z" fill="#8f74bd"/></marker>
    <marker id="a-small" viewBox="0 0 10 10" refX="8" refY="5" markerWidth="4" markerHeight="4" orient="auto"><path d="M0 0 L10 5 L0 10 Z" fill="#111"/></marker>

    <polygon id="star" points="0,-112 21.2,-79.2 56,-97 58,-58 97,-56 79.2,-21.2 112,0 79.2,21.2 97,56 58,58 56,97 21.2,79.2 0,112 -21.2,79.2 -56,97 -58,58 -97,56 -79.2,21.2 -112,0 -79.2,-21.2 -97,-56 -58,-58 -56,-97 -21.2,-79.2"/>

    <g id="sat-dark"><line class="spoke" x1="140" x2="175" y1="0" y2="0"/><circle class="sat-ring" cx="210" cy="0" r="38"/><circle class="sat-white" cx="210" cy="0" r="35"/><circle class="sat-dark" cx="210" cy="0" r="30"/></g>
    <g id="sat-blue"><line class="spoke" x1="140" x2="175" y1="0" y2="0"/><circle class="sat-ring" cx="210" cy="0" r="38"/><circle class="sat-white" cx="210" cy="0" r="35"/><circle class="sat-blue" cx="210" cy="0" r="30"/></g>
    <g id="sat-purple"><line class="spoke" x1="140" x2="175" y1="0" y2="0"/><circle class="sat-ring" cx="210" cy="0" r="38"/><circle class="sat-white" cx="210" cy="0" r="35"/><circle class="sat-purple" cx="210" cy="0" r="30"/></g>
  </defs>

  <rect width="2325" height="1568" fill="var(--bg)"/>

  <!-- Connectors -->
  <g class="connectors">
    <polyline class="dash orange" points="385,368 385,432 725,432 955,665" marker-end="url(#a-orange)"/>
    <polyline class="dash black" points="398,368 398,444 785,444 975,638" marker-end="url(#a-black)"/>
    <polyline class="dash black" points="760,258 818,258 818,432 1000,612" marker-end="url(#a-black)"/>
    <polyline class="dash black" points="1550,258 1492,258 1492,432 1310,612" marker-end="url(#a-black)"/>
    <polyline class="dash black" points="1912,368 1912,444 1525,444 1335,638" marker-end="url(#a-black)"/>
    <polyline class="dash green" points="1925,368 1925,432 1585,432 1355,665" marker-end="url(#a-green)"/>
    <line class="dash black" x1="1155" y1="556" x2="1155" y2="420" marker-end="url(#a-black)"/>
    <line class="dash black" x1="925" y1="783" x2="790" y2="783" marker-end="url(#a-black)"/>
    <line class="dash black" x1="470" y1="783" x2="338" y2="783" marker-end="url(#a-black)"/>
    <line class="dash black" x1="1383" y1="783" x2="1520" y2="783" marker-end="url(#a-black)"/>
    <line class="dash black" x1="1164" y1="1012" x2="1164" y2="1148" marker-end="url(#a-black)"/>
    <line class="dash purple" x1="1147" y1="1150" x2="1147" y2="1014" marker-end="url(#a-purple)"/>
    <polyline class="dash red" points="965,910 770,1107 478,1107 390,1206" marker-end="url(#a-red)"/>
    <line class="dash red" x1="980" y1="932" x2="714" y2="1203" marker-end="url(#a-red)"/>
    <line class="dash red" x1="1327" y1="932" x2="1593" y2="1203" marker-end="url(#a-red)"/>
    <polyline class="dash black" points="755,1368 995,1368 995,1360" marker-end="url(#a-black)"/>
    <polyline class="dash black" points="1552,1368 1312,1368 1312,1360" marker-end="url(#a-black)"/>
  </g>

  <!-- State societies -->
  <g class="unit sos">
    <rect class="frame" x="28" y="178" width="204" height="158" rx="10"/>
    <rect x="38" y="188" width="184" height="138" fill="var(--orange)" role="img" aria-label="Map of the fifty states"/>
    <text class="unit-label xl" x="130" y="258">SOS</text>
  </g>

  <!-- Top committee boxes -->
  <g class="unit boc">
    <rect x="290" y="155" width="205" height="203" rx="32" fill="#fff" stroke="#111" stroke-width="3"/>
    <rect x="300" y="165" width="185" height="183" rx="26" fill="url(#g-orange)"/>
    <text class="unit-label xl" x="393" y="258">BOC</text>
  </g>
  <g class="unit ceoi">
    <rect x="547" y="155" width="205" height="203" rx="32" fill="#fff" stroke="#111" stroke-width="3"/>
    <rect x="557" y="165" width="185" height="183" rx="26" fill="url(#g-dark)"/>
    <text class="unit-label xl" x="649" y="258">CEOI</text>
  </g>
  <g class="unit pcp">
    <rect x="1559" y="155" width="205" height="203" rx="32" fill="#fff" stroke="#111" stroke-width="3"/>
    <rect x="1569" y="165" width="185" height="183" rx="26" fill="url(#g-dark)"/>
    <text class="unit-label xl" x="1661" y="258">PCP</text>
  </g>
  <g class="unit bos">
    <rect x="1815" y="155" width="205" height="203" rx="32" fill="#fff" stroke="#111" stroke-width="3"/>
    <rect x="1825" y="165" width="185" height="183" rx="26" fill="url(#g-green)"/>
    <text class="unit-label xl" x="1917" y="258">BOS</text>
  </g>
  <line class="dash black" x1="2075" y1="258" x2="2030" y2="258" marker-end="url(#a-black)"/>

  <!-- Specialty societies grid -->
  <g class="specialty-societies">
    <rect class="frame" x="2078" y="93" width="220" height="328" rx="14"/>
    <g>
      <rect class="society-cell" x="2088" y="103" width="62" height="38" rx="5"/><text class="society-label" x="2119" y="122">BRTWQ</text>
      <rect class="society-cell" x="2156" y="103" width="62" height="38" rx="5"/><text class="society-label" x="2187" y="122">GLU</text>
      <rect class="society-cell" x="2225" y="103" width="62" height="38" rx="5"/><text class="society-label" x="2256" y="122">PWIB</text>
      <rect class="society-cell" x="2088" y="148" width="62" height="38" rx="5"/><text class="society-label" x="2119" y="167">NUDO</text>
      <rect class="society-cell" x="2156" y="148" width="62" height="38" rx="5"/><text class="society-label" x="2187" y="167">EV</text>
      <rect class="society-cell" x="2225" y="148" width="62" height="38" rx="5"/><text class="society-label" x="2256" y="167">YT</text>
      <rect class="society-cell" x="2088" y="193" width="62" height="38" rx="5"/><text class="society-label" x="2119" y="212">FWUL</text>
      <rect class="society-cell" x="2156" y="193" width="62" height="38" rx="5"/><text class="society-label" x="2187" y="212">ZQMEU</text>
      <rect class="society-cell" x="2225" y="193" width="62" height="38" rx="5"/><text class="society-label" x="2256" y="212">DBIW</text>
      <rect class="society-cell" x="2088" y="238" width="62" height="38" rx="5"/><text class="society-label" x="2119" y="257">TIGK</text>
      <rect class="society-cell" x="2156" y="238" width="62" height="38" rx="5"/><text class="society-label" x="2187" y="257">UFBZK</text>
      <rect class="society-cell" x="2225" y="238" width="62" height="38" rx="5"/><text class="society-label" x="2256" y="257">IWNLE</text>
      <rect class="society-cell" x="2088" y="283" width="62" height="38" rx="5"/><text class="society-label" x="2119" y="302">ZCKW</text>
      <rect class="society-cell" x="2156" y="283" width="62" height="38" rx="5"/><text class="society-label" x="2187" y="302">VHYU</text>
      <rect class="society-cell" x="2225" y="283" width="62" height="38" rx="5"/><text class="society-label" x="2256" y="302">NGBE</text>
      <rect class="society-cell" x="2088" y="328" width="62" height="38" rx="5"/><text class="society-label" x="2119" y="347">TKW</text>
      <rect class="society-cell" x="2156" y="328" width="62" height="38" rx="5"/><text class="society-label" x="2187" y="347">DUWO</text>
      <rect class="society-cell" x="2225" y="328" width="62" height="38" rx="5"/><text class="society-label" x="2256" y="347">QETF</text>
      <rect class="society-cell" x="2088" y="373" width="62" height="38" rx="5"/><text class="society-label" x="2119" y="392">UWB</text>
      <rect class="society-cell" x="2156" y="373" width="62" height="38" rx="5"/><text class="society-label" x="2187" y="392">KIPEW</text>
      <rect class="society-cell" x="2225" y="373" width="62" height="38" rx="5"/><text class="society-label" x="2256" y="392">BWH</text>
    </g>
  </g>

  <!-- Councils -->
  <g class="council education" transform="translate(1155,258)">
    <g role="img" aria-label="Ten education subcommittees">
      <use href="#sat-dark" transform="rotate(0)"/><use href="#sat-dark" transform="rotate(36)"/><use href="#sat-dark" transform="rotate(72)"/><use href="#sat-dark" transform="rotate(108)"/><use href="#sat-dark" transform="rotate(144)"/><use href="#sat-dark" transform="rotate(180)"/><use href="#sat-dark" transform="rotate(216)"/><use href="#sat-dark" transform="rotate(252)"/><use href="#sat-dark" transform="rotate(288)"/><use href="#sat-dark" transform="rotate(324)"/>
    </g>
    <circle r="152" fill="#fff" stroke="#111" stroke-width="3"/>
    <circle r="142" fill="url(#g-dark)"/>
    <text class="unit-label md" y="0">EDUCATION</text>
  </g>

  <g class="council advocacy" transform="translate(628,783)">
    <g role="img" aria-label="Ten advocacy subcommittees">
      <use href="#sat-blue" transform="rotate(18)"/><use href="#sat-blue" transform="rotate(54)"/><use href="#sat-blue" transform="rotate(90)"/><use href="#sat-blue" transform="rotate(126)"/><use href="#sat-blue" transform="rotate(162)"/><use href="#sat-blue" transform="rotate(198)"/><use href="#sat-blue" transform="rotate(234)"/><use href="#sat-blue" transform="rotate(270)"/><use href="#sat-blue" transform="rotate(306)"/><use href="#sat-blue" transform="rotate(342)"/>
    </g>
    <circle r="152" fill="#fff" stroke="#111" stroke-width="3"/>
    <circle r="142" fill="url(#g-blue)"/>
    <text class="unit-label md" y="0">ADVOCACY</text>
  </g>

  <g class="council research" transform="translate(1682,783)">
    <g role="img" aria-label="Ten research and quality subcommittees">
      <use href="#sat-dark" transform="rotate(18)"/><use href="#sat-dark" transform="rotate(54)"/><use href="#sat-dark" transform="rotate(90)"/><use href="#sat-dark" transform="rotate(126)"/><use href="#sat-dark" transform="rotate(162)"/><use href="#sat-dark" transform="rotate(198)"/><use href="#sat-dark" transform="rotate(234)"/><use href="#sat-dark" transform="rotate(270)"/><use href="#sat-dark" transform="rotate(306)"/><use href="#sat-dark" transform="rotate(342)"/>
    </g>
    <circle r="152" fill="#fff" stroke="#111" stroke-width="3"/>
    <circle r="142" fill="url(#g-dark)"/>
    <text class="unit-label md" y="-22">RESEARCH</text>
    <text class="unit-label md" y="18">&amp; QUALITY</text>
  </g>

  <g class="council membership" transform="translate(1155,1310)">
    <g role="img" aria-label="Ten membership subcommittees">
      <use href="#sat-purple" transform="rotate(0)"/><use href="#sat-purple" transform="rotate(36)"/><use href="#sat-purple" transform="rotate(72)"/><use href="#sat-purple" transform="rotate(108)"/><use href="#sat-purple" transform="rotate(144)"/><use href="#sat-purple" transform="rotate(180)"/><use href="#sat-purple" transform="rotate(216)"/><use href="#sat-purple" transform="rotate(252)"/><use href="#sat-purple" transform="rotate(288)"/><use href="#sat-purple" transform="rotate(324)"/>
    </g>
    <circle r="152" fill="#fff" stroke="#111" stroke-width="3"/>
    <circle r="142" fill="url(#g-purple)"/>
    <text class="unit-label md" y="0">MEMBERSHIP</text>
  </g>

  <g class="council coa" transform="translate(177,783)">
    <circle r="150" fill="#fff" stroke="#111" stroke-width="3"/>
    <circle r="140" fill="url(#g-blue)"/>
    <text class="unit-label xl" y="0">COA</text>
  </g>

  <!-- Board of Directors -->
  <g class="board" transform="translate(1155,783)">
    <circle r="224" fill="#fff" stroke="#111" stroke-width="3"/>
    <path fill="var(--red)" d="M -184.9 -115.5 A 218 218 0 0 1 184.9 -115.5 L 127.2 -79.5 A 150 150 0 0 0 -127.2 -79.5 Z"/>
    <path fill="var(--green)" d="M 184.9 -115.5 A 218 218 0 0 1 202.1 81.7 L 139.1 56.2 A 150 150 0 0 0 127.2 -79.5 Z"/>
    <path fill="var(--purple)" d="M 202.1 81.7 A 218 218 0 0 1 -202.1 81.7 L -139.1 56.2 A 150 150 0 0 0 139.1 56.2 Z"/>
    <path fill="var(--orange)" d="M -202.1 81.7 A 218 218 0 0 1 -184.9 -115.5 L -127.2 -79.5 A 150 150 0 0 0 -139.1 56.2 Z"/>
    <circle r="150" fill="#fff" stroke="#111" stroke-width="3"/>
    <circle r="141" fill="url(#g-dark)"/>
    <rect x="-110" y="-110" width="220" height="108" rx="6" fill="url(#g-stone)" opacity="0.85" role="img" aria-label="Headquarters building"/>
    <text class="unit-label lg" y="34">THE BOARD OF</text>
    <text class="unit-label lg" y="74">DIRECTORS</text>
  </g>
  <g class="board-seats" role="img" aria-label="Sixteen board seats">
    <circle class="seat" cx="1056" cy="632" r="22" stroke="var(--red-dark)"/>
    <circle class="seat" cx="1120" cy="604" r="22" stroke="var(--red-dark)"/>
    <circle class="seat" cx="1190" cy="604" r="22" stroke="var(--red-dark)"/>
    <circle class="seat" cx="1254" cy="632" r="22" stroke="var(--red-dark)"/>
    <circle class="seat" cx="1005" cy="683" r="22" stroke="var(--orange-dark)"/>
    <circle class="seat" cx="978" cy="748" r="22" stroke="var(--orange-dark)"/>
    <circle class="seat" cx="978" cy="818" r="22" stroke="var(--orange-dark)"/>
    <circle class="seat" cx="1305" cy="683" r="22" stroke="var(--green-dark)"/>
    <circle class="seat" cx="1332" cy="748" r="22" stroke="var(--green-dark)"/>
    <circle class="seat" cx="1332" cy="818" r="22" stroke="var(--green-dark)"/>
    <circle class="seat" cx="1006" cy="882" r="22" stroke="var(--purple-dark)"/>
    <circle class="seat" cx="1056" cy="932" r="22" stroke="var(--purple-dark)"/>
    <circle class="seat" cx="1120" cy="957" r="22" stroke="var(--purple-dark)"/>
    <circle class="seat" cx="1190" cy="957" r="22" stroke="var(--purple-dark)"/>
    <circle class="seat" cx="1254" cy="932" r="22" stroke="var(--purple-dark)"/>
    <circle class="seat" cx="1304" cy="882" r="22" stroke="var(--purple-dark)"/>
  </g>

  <!-- Nominating Committee -->
  <g class="unit nc">
    <g transform="translate(285,1310)">
      <line class="burst-arrow" x1="168" y1="0" x2="128" y2="0" marker-end="url(#a-small)"/>
      <line class="burst-arrow" x1="168" y1="0" x2="128" y2="0" transform="rotate(90)" marker-end="url(#a-small)"/>
      <line class="burst-arrow" x1="168" y1="0" x2="128" y2="0" transform="rotate(180)" marker-end="url(#a-small)"/>
      <line class="burst-arrow" x1="168" y1="0" x2="128" y2="0" transform="rotate(270)" marker-end="url(#a-small)"/>
      <line class="burst-arrow" x1="195" y1="0" x2="160" y2="0" transform="rotate(45)" marker-end="url(#a-small)"/>
      <line class="burst-arrow" x1="195" y1="0" x2="160" y2="0" transform="rotate(135)" marker-end="url(#a-small)"/>
      <line class="burst-arrow" x1="195" y1="0" x2="160" y2="0" transform="rotate(225)" marker-end="url(#a-small)"/>
      <line class="burst-arrow" x1="195" y1="0" x2="160" y2="0" transform="rotate(315)" marker-end="url(#a-small)"/>
    </g>
    <rect x="183" y="1200" width="205" height="220" rx="32" fill="#fff" stroke="#111" stroke-width="3"/>
    <rect x="193" y="1210" width="185" height="200" rx="26" fill="url(#g-red)"/>
    <text class="unit-label xl" x="285" y="1257">NC</text>
    <g role="img" aria-label="Six committee seats">
      <circle cx="236" cy="1320" r="21" fill="var(--orange)" stroke="#fff" stroke-width="4"/>
      <circle cx="286" cy="1320" r="21" fill="var(--purple)" stroke="#fff" stroke-width="4"/>
      <circle cx="336" cy="1320" r="21" fill="var(--purple)" stroke="#fff" stroke-width="4"/>
      <circle cx="236" cy="1368" r="21" fill="var(--green)" stroke="#fff" stroke-width="4"/>
      <circle cx="286" cy="1368" r="21" fill="var(--purple)" stroke="#fff" stroke-width="4"/>
      <circle cx="336" cy="1368" r="21" fill="var(--purple)" stroke="#fff" stroke-width="4"/>
    </g>
  </g>

  <!-- Bylaws and Resolutions Committees -->
  <g class="unit bc" transform="translate(645,1310)">
    <g>
      <line class="burst-arrow" x1="122" x2="152" y1="0" y2="0" transform="rotate(15)" marker-end="url(#a-small)"/>
      <line class="burst-arrow" x1="122" x2="152" y1="0" y2="0" transform="rotate(45)" marker-end="url(#a-small)"/>
      <line class="burst-arrow" x1="122" x2="152" y1="0" y2="0" transform="rotate(75)" marker-end="url(#a-small)"/>
      <line class="burst-arrow" x1="122" x2="152" y1="0" y2="0" transform="rotate(105)" marker-end="url(#a-small)"/>
      <line class="burst-arrow" x1="122" x2="152" y1="0" y2="0" transform="rotate(135)" marker-end="url(#a-small)"/>
      <line class="burst-arrow" x1="122" x2="152" y1="0" y2="0" transform="rotate(165)" marker-end="url(#a-small)"/>
      <line class="burst-arrow" x1="122" x2="152" y1="0" y2="0" transform="rotate(195)" marker-end="url(#a-small)"/>
      <line class="burst-arrow" x1="122" x2="152" y1="0" y2="0" transform="rotate(225)" marker-end="url(#a-small)"/>
      <line class="burst-arrow" x1="122" x2="152" y1="0" y2="0" transform="rotate(255)" marker-end="url(#a-small)"/>
      <line class="burst-arrow" x1="122" x2="152" y1="0" y2="0" transform="rotate(285)" marker-end="url(#a-small)"/>
      <line class="burst-arrow" x1="122" x2="152" y1="0" y2="0" transform="rotate(315)" marker-end="url(#a-small)"/>
      <line class="burst-arrow" x1="122" x2="152" y1="0" y2="0" transform="rotate(345)" marker-end="url(#a-small)"/>
    </g>
    <use href="#star" fill="#fff" stroke="#111" stroke-width="3"/>
    <use href="#star" transform="scale(0.9)" fill="url(#g-red)"/>
    <text class="unit-label xl" y="0">BC</text>
  </g>
  <g class="unit rc" transform="translate(1660,1310)">
    <g>
      <line class="burst-arrow" x1="122" x2="152" y1="0" y2="0" transform="rotate(15)" marker-end="url(#a-small)"/>
      <line class="burst-arrow" x1="122" x2="152" y1="0" y2="0" transform="rotate(45)" marker-end="url(#a-small)"/>
      <line class="burst-arrow" x1="122" x2="152" y1="0" y2="0" transform="rotate(75)" marker-end="url(#a-small)"/>
      <line class="burst-arrow" x1="122" x2="152" y1="0" y2="0" transform="rotate(105)" marker-end="url(#a-small)"/>
      <line class="burst-arrow" x1="122" x2="152" y1="0" y2="0" transform="rotate(135)" marker-end="url(#a-small)"/>
      <line class="burst-arrow" x1="122" x2="152" y1="0" y2="0" transform="rotate(165)" marker-end="url(#a-small)"/>
      <line class="burst-arrow" x1="122" x2="152" y1="0" y2="0" transform="rotate(195)" marker-end="url(#a-small)"/>
      <line class="burst-arrow" x1="122" x2="152" y1="0" y2="0" transform="rotate(225)" marker-end="url(#a-small)"/>
      <line class="burst-arrow" x1="122" x2="152" y1="0" y2="0" transform="rotate(255)" marker-end="url(#a-small)"/>
      <line class="burst-arrow" x1="122" x2="152" y1="0" y2="0" transform="rotate(285)" marker-end="url(#a-small)"/>
      <line class="burst-arrow" x1="122" x2="152" y1="0" y2="0" transform="rotate(315)" marker-end="url(#a-small)"/>
      <line class="burst-arrow" x1="122" x2="152" y1="0" y2="0" transform="rotate(345)" marker-end="url(#a-small)"/>
    </g>
    <use href="#star" fill="#fff" stroke="#111" stroke-width="3"/>
    <use href="#star" transform="scale(0.9)" fill="url(#g-red)"/>
    <text class="unit-label xl" y="0">RC</text>
  </g>

  <!-- Seat legend -->
  <g class="legend">
    <rect class="frame" x="1975" y="567" width="323" height="433" rx="22"/>
    <circle cx="2015" cy="617" r="20" fill="var(--red)"/><text class="key-text" x="2050" y="625">President</text>
    <circle cx="2015" cy="673" r="20" fill="var(--red)"/><text class="key-text" x="2050" y="681">1st Vice Presidents</text>
    <circle cx="2015" cy="729" r="20" fill="var(--red)"/><text class="key-text" x="2050" y="737">2nd Vice Presidents</text>
    <circle cx="2015" cy="784" r="20" fill="var(--red)"/><text class="key-text" x="2050" y="792">The Past President</text>
    <circle cx="2015" cy="840" r="20" fill="var(--orange)"/><text class="key-text" x="2050" y="848">Appointed by BOC</text>
    <circle cx="2015" cy="896" r="20" fill="var(--green)"/><text class="key-text" x="2050" y="904">Appointed by BOS</text>
    <circle cx="2015" cy="952" r="20" fill="var(--purple)"/><text class="key-text" x="2050" y="960">Appointed by Members</text>
  </g>

  <!-- Glossary -->
  <g class="glossary">
    <rect class="frame" x="1867" y="1093" width="431" height="434" rx="30"/>
    <text class="key-text" x="1885" y="1143">-</text><text class="key-text" x="1905" y="1143">Council on Advocacy (COA)</text>
    <text class="key-text" x="1885" y="1172">-</text><text class="key-text" x="1905" y="1172">Political Action Committee (PAC)</text>
    <text class="key-text" x="1885" y="1201">-</text><text class="key-text" x="1905" y="1201">Committee on Ethics and Outside</text>
    <text class="key-text" x="1905" y="1230">Interests (CEOI)</text>
    <text class="key-text" x="1885" y="1259">-</text><text class="key-text" x="1905" y="1259">Board of Councilors (BOC)</text>
    <text class="key-text" x="1885" y="1288">-</text><text class="key-text" x="1905" y="1288">Board of Specialty Societies (BOS)</text>
    <text class="key-text" x="1885" y="1317">-</text><text class="key-text" x="1905" y="1317">Professional Compliance</text>
    <text class="key-text" x="1905" y="1346">Program (PCP)</text>
    <text class="key-text" x="1885" y="1375">-</text><text class="key-text" x="1905" y="1375">Nominating Committee (NC)</text>
    <text class="key-text" x="1885" y="1404">-</text><text class="key-text" x="1905" y="1404">Bylaws Committee (BC)</text>
    <text class="key-text" x="1885" y="1433">-</text><text class="key-text" x="1905" y="1433">Resolutions Committee (RC)</text>
    <text class="key-text" x="1885" y="1462">-</text><text class="key-text" x="1905" y="1462">100 members appointed by societies</text>
    <text class="key-text" x="1905" y="1491">in each of the 50 states (SOS)</text>
  </g>
</svg>
</body>
</html>
```